Dermatopathology Brochure

We need a brochure that will let potential clients know our services. It needs to be clean, clear, and eye-catching. A modern feel is what we would like. Some previous work done for us in the past has been included. We have uploaded a word file with content as well. You may also use information from our website, skinslidecrest.com. You don't have to use all available information, but the content of the word file is our main message.
Updates

Although the postcard highlights our MeetPlume based online clinicopathologic correlation, we would like our brochure to be more general. In other words, we use postcards to make a single important point, but the brochure should be more balanced regarding our services. Also, the postcard was great for us, but we don't necessarily want to repeat its look exactly. We liked the postacard's clean and balanced look. We would like to try having our brochure more "friendly" and conversational, yet professional. Thanks!

Target Market(s)

Physicians, mostly dermatologists.

Industry/Entity Type

Work

```html
<!DOCTYPE html>
<html lang="en">
<head>
<meta charset="utf-8">
<title>Crestline Skin Pathology Associates – Brochure</title>
<link href="https://fonts.googleapis.com/css2?family=Open+Sans:wght@400;600;700;800&display=swap" rel="stylesheet">
<style>
:root{
  --red:#d3141b;
  --red-dark:#8e0c10;
  --ink:#231f20;
  --charcoal:#2a2627;
  --paper:#ffffff;
  --stage:#5c5c5c;
  --text:#3b3b3b;
}
*{margin:0;padding:0;box-sizing:border-box}
html,body{width:1200px;height:829px;overflow:hidden}
body{background:var(--stage);font-family:"Open Sans",Arial,sans-serif;color:var(--text);position:relative}

/* ---------- cover ---------- */
.cover{position:absolute;left:30px;top:150px;width:380px;height:560px;background:var(--charcoal);overflow:hidden}
.cover__art{position:absolute;left:0;top:0;width:380px;height:330px}
.cover__brand{position:absolute;left:22px;top:350px;display:flex;align-items:center;gap:8px;color:var(--paper);font-weight:700;font-size:13px;letter-spacing:.5px}
.cover__brand-dot{width:14px;height:14px;border-radius:50%;background:var(--red)}
.cover__title{position:absolute;left:22px;top:386px;font-weight:800;font-size:24px;line-height:1.1;color:var(--paper);letter-spacing:-.5px;white-space:nowrap}
.cover__title .accent{color:var(--red)}
.cover__text{position:absolute;left:22px;top:430px;width:336px;font-size:9.6px;line-height:1.4;color:#e6e6e6}

/* ---------- inside spread ---------- */
.spread{position:absolute;left:440px;top:150px;width:730px;height:520px;background:var(--paper);display:flex}
.page{position:relative;width:365px;height:100%}
.page--left{border-right:1px solid #d8d8d8;display:flex}
.about{width:150px;height:100%;background:var(--red);padding:28px 12px 0 14px;color:var(--paper)}
.about__title{font-weight:800;font-size:22px;margin-bottom:8px}
.about__text{font-size:8px;line-height:1.45;text-align:justify}
.feature{flex:1;padding:16px 12px 0 12px}
.feature__scope{width:124px;height:124px;border-radius:50%;display:block;margin:0 0 16px 8px}
.feature__title{font-weight:800;font-size:20px;color:var(--ink);margin-bottom:6px}
.feature__title .accent{color:var(--red)}
.feature__text{font-size:8.2px;line-height:1.45;text-align:justify;color:var(--ink)}

.masthead{margin:14px 12px 0 12px;height:66px;background:var(--ink);display:flex;align-items:center;padding:0 10px 0 6px;gap:10px}
.masthead__portrait{width:60px;height:56px;background:linear-gradient(160deg,#9aa7b8,#44526a)}
.masthead__firm{color:var(--paper);font-weight:700;font-size:12px;line-height:1.2}
.masthead__doctor{color:var(--red);font-weight:800;font-size:14px;margin-top:3px}
.service{margin:12px 18px 0 18px}
.service__title{font-weight:800;font-size:12px;color:var(--ink);text-transform:uppercase}
.service__title .accent{color:var(--red);text-transform:none}
.service__text{font-size:7.6px;line-height:1.45;margin-top:4px;color:var(--text)}
.callout{position:absolute;left:40px;right:14px;top:318px;background:linear-gradient(160deg,var(--red),var(--red-dark));padding:12px 14px 14px;color:var(--paper)}
.callout__title{font-weight:800;font-size:18px;line-height:1.2;margin-bottom:6px}
.callout__title .dark{color:var(--ink)}
.callout__cols{display:flex;gap:14px}
.callout__cols p{flex:1;font-size:7.4px;line-height:1.38;text-align:justify}
</style>
</head>
<body>

<section class="cover">
  <svg class="cover__art" viewBox="0 0 380 330" role="img" aria-label="Micrograph of stained skin tissue">
    <defs>
      <linearGradient id="tissue" x1="0" y1="0" x2="1" y2="1">
        <stop offset="0" stop-color="#f5dcc0"/>
        <stop offset=".45" stop-color="#d98a9a"/>
        <stop offset="1" stop-color="#a24f78"/>
      </linearGradient>
      <linearGradient id="swoosh" x1="0" y1="0" x2="1" y2="0">
        <stop offset="0" stop-color="#8e0c10"/>
        <stop offset=".5" stop-color="#d3141b"/>
        <stop offset="1" stop-color="#8e0c10"/>
      </linearGradient>
    </defs>
    <path d="M0 0H380V250C300 330 120 330 0 230Z" fill="url(#swoosh)"/>
    <path d="M0 0H380V228C300 306 120 306 0 210Z" fill="#ffffff"/>
    <path d="M0 0H380V220C300 296 120 296 0 202Z" fill="url(#tissue)"/>
  </svg>
  <div class="cover__brand"><span class="cover__brand-dot"></span>CRESTLINE SKIN PATHOLOGY</div>
  <h1 class="cover__title">THE DIAGNOSIS <span class="accent">IN FOCUS</span></h1>
  <p class="cover__text">We know how important reliable dermatopathology services are to your patients and your practice. As your partner in patient care, we want to do our part in helping you arrive at the diagnosis for each patient you entrust to us. We also know that part of our job is making working with us as smooth as possible. We can provide courier pick up service to local practices, and we will help arrange overnight delivery for specimens sent from outside our area. We'll handle the details so you can focus on the care of your patients.</p>
</section>

<section class="spread">
  <div class="page page--left">
    <div class="about">
      <h2 class="about__title">ABOUT US</h2>
      <p class="about__text">Lorem ipsum dolor sit amet, consectetuer adipiscing elit. Aenean commodo ligula eget dolor. Aenean massa. Cum sociis natoque penatibus et magnis dis parturient montes, nascetur ridiculus mus. Donec quam felis, ultricies nec, pellentesque eu, pretium quis, sem. Nulla consequat massa quis enim. Donec pede justo, fringilla vel, aliquet nec, vulputate eget, arcu. In enim justo, rhoncus ut, imperdiet a, venenatis vitae, justo. Nullam dictum felis eu pede mollis pretium. Integer tincidunt. Cras dapibus. Vivamus elementum semper nisi. Aenean vulputate eleifend tellus. Aenean leo ligula, porttitor eu, consequat vitae, eleifend ac, enim. Aliquam lorem ante, dapibus in, viverra quis, feugiat a, tellus. Phasellus viverra nulla ut metus varius laoreet.</p>
    </div>
    <div class="feature">
      <svg class="feature__scope" viewBox="0 0 124 124" role="img" aria-label="Circular microscope view of a tissue slide">
        <defs>
          <radialGradient id="slide" cx=".45" cy=".45" r=".6">
            <stop offset="0" stop-color="#f2c9b6"/>
            <stop offset=".6" stop-color="#d98a9a"/>
            <stop offset="1" stop-color="#a24f78"/>
          </radialGradient>
        </defs>
        <rect width="124" height="124" fill="#111"/>
        <circle cx="62" cy="62" r="58" fill="url(#slide)"/>
      </svg>
      <h2 class="feature__title">LOREM <span class="accent">IPSUM</span></h2>
      <p class="feature__text">Lorem ipsum dolor sit amet, consectetuer adipiscing elit. Aenean commodo ligula eget dolor. Aenean massa. Cum sociis natoque penatibus et magnis dis parturient montes, nascetur ridiculus mus. Donec quam felis, ultricies nec, pellentesque eu, pretium quis, sem. Nulla consequat massa quis enim. Donec pede justo, fringilla vel, aliquet nec, vulputate eget, arcu. In enim justo, rhoncus ut, imperdiet a, venenatis vitae, justo. Nullam dictum felis eu pede mollis pretium. Integer tincidunt. Cras dapibus. Vivamus elementum semper nisi. Aenean vulputate eleifend tellus. Aenean leo ligula, porttitor eu, consequat vitae, eleifend ac, enim. Aliquam lorem ante, dapibus in, viverra quis, feugiat a, tellus. Phasellus viverra nulla ut metus varius laoreet. Quisque rutrum. Aenean imperdiet. Etiam ultricies nisi vel augue. Curabitur ullamcorper ultricies nisi. Nam eget dui. Etiam rhoncus. Maecenas tempus, tellus eget condimentum rhoncus, sem quam semper libero, sit amet adipiscing sem neque sed ipsum. Nam quam nunc, blandit vel, luctus pulvinar, hendrerit id, lorem. Maecenas nec odio et ante tincidunt tempus. Donec vitae sapien ut libero venenatis faucibus. Nullam quis.</p>
    </div>
  </div>

  <div class="page page--right">
    <header class="masthead">
      <div class="masthead__portrait" role="img" aria-label="Portrait photo of the dermatopathologist"></div>
      <div>
        <div class="masthead__firm">Crestline Skin Pathology<br>Associates, Inc.</div>
        <div class="masthead__doctor">LENA M. HARLOW, M.D.</div>
      </div>
    </header>

    <div class="service">
      <h3 class="service__title">Expertise – <span class="accent">academic teaching hospitals to private practice</span></h3>
      <p class="service__text">Dr. Harlow has worked as a consultant dermatopathologist for the Westbrook University Department of Dermatology, interpreting challenging cases from the teaching hospital floors and academic dermatologist offices. She has, and continues to provide interpretations for dermatologists in typical private practice as well.</p>
    </div>
    <div class="service">
      <h3 class="service__title">Availability - <span class="accent">we're here for you and your patients</span></h3>
      <p class="service__text">We believe the flow of information between treating physician and consultant dermatopathologist is vital for high quality patient care. That's why whether on the phone or using 21st Century communication technology, such as web-based clinicopathologic conferencing, we want to hear what you have to say.</p>
    </div>
    <div class="service">
      <h3 class="service__title">Connectivity - <span class="accent">making your workflow easier</span></h3>
      <p class="service__text">Depending on your medical record system, we can mail, fax, or directly upload reports into your electronic medical records. Paper or electronic, we'll try to make your workflow easier.</p>
    </div>

    <aside class="callout">
      <h2 class="callout__title"><span class="dark">LOREM</span> IPSUM</h2>
      <div class="callout__cols">
        <p>Lorem ipsum dolor sit amet, consectetuer adipiscing elit. Aenean commodo ligula eget dolor. Aenean massa. Cum ntes, nascetur ridiculus mus. Donec quam felis, ultricies nec, pellentesque eu, pretium quis, sem. Nulla consequat massa quis enim. Donec pede justo, fringilla vel, aliquet nec, vulputate eget, arcu. In enim justo a, venenatis vitae, justo. Nullam dictum felis euuis.</p>
        <p>Lorem ipsum dolor sit amet, consectetuer adipiscing elit. Aenean commodo ligula eget dolor. Aenean massa. Cum ntes, nascetur ridiculus mus. Donec quam felis, ultricies nec, pellentesque eu, pretium quis, sem. Nulla consequat massa quis enim. Donec pede justo, fringilla vel, aliquet nec, vulputate eget, arcu. In enim justo a, venenatis vitae, justo. Nullam dictum felis euuis.</p>
      </div>
    </aside>
  </div>
</section>

</body>
</html>
```